Tallow & Mersey Needs New Stationery / Letterhead Design

We need new stationery to match our new logo (attached). Tallow & Mersey is a 34 year old nationwide law firm located in Houston Tx. They do personal injury law and pharmaceutical litigation.

WE DO NOT NEED BUSINESS CARDS.

Attached are several different file formats of the new logo.

Reason: We will make a decision in the next couple days. Finalizing edits now. Thank you!

Target Market(s)

consumers who have been injured due to the negligence of another or by a pharmaceutical drug or defective medical device. Also co-counsel and opposing counsel (law firms0.

Industry/Entity Type

Law Firm

Requirements
Must have
• logo
• Tallow & Mersey, LLP
• 7183 Corvid Lane, Suite 1000
• Brenford, TX 75591
• Tel: (555) 408-1936
• Fax: (555) 408-2275
• www.tallowandmersey.example
• Must have colors in the logo.
• Make the font go with the logo - not necessarily the same, but something that goes well with it.

```html
<!DOCTYPE html>
<html lang="en">
<head>
<meta charset="utf-8">
<title>Tallow &amp; Mersey Stationery</title>
<link href="https://fonts.googleapis.com/css2?family=Montserrat:wght@400;600&display=swap" rel="stylesheet">
<style>
  :root {
    --bg: #a8a39f;
    --paper: #ffffff;
    --navy: #24305a;
    --ink: #222222;
    --grey: #55596a;
    --faint: #c9cbd8;
    --shade: #e6e6ea;
    --flap: #ececf0;
    --pocket: #f4f4f6;
  }
  * { box-sizing: border-box; margin: 0; padding: 0; }
  html, body { width: 1200px; height: 1200px; overflow: hidden; }
  body { background: var(--bg); position: relative; font-family: "Montserrat", sans-serif; }

  .brand {
    font-family: "Montserrat", sans-serif; font-weight: 600; color: var(--navy);
    display: flex; align-items: center; gap: 6px; white-space: nowrap;
  }
  .brand .square { width: 12px; height: 12px; background: var(--navy); flex: none; }
  .header { display: flex; justify-content: space-between; align-items: flex-start; }
  .contact { text-align: right; font-size: 7px; color: var(--grey); line-height: 1.55; white-space: nowrap; }
  .contact .firm { font-weight: 600; font-size: 8.5px; color: var(--navy); margin-bottom: 2px; }
  .contact svg { width: 6px; height: 6px; vertical-align: middle; margin-left: 3px; fill: var(--navy); }
  .address { position: absolute; left: 0; right: 0; text-align: center; color: var(--navy); white-space: nowrap; }

  /* Letterhead */
  .letterhead {
    position: absolute; left: 549px; top: 163px; width: 458px; height: 591px;
    background: var(--paper); box-shadow: 0 6px 14px rgba(0,0,0,.25);
    padding: 28px 30px 0;
  }
  .letterhead .brand { font-size: 13px; }
  .letterhead .header { padding-top: 8px; }
  .body { margin-top: 120px; font-size: 6.2px; line-height: 1.8; color: var(--ink); }
  .body p { margin-bottom: 10px; }
  .closing { margin-top: 4px; }
  .signature { margin-top: 6px; width: 90px; height: 28px; background: linear-gradient(90deg, #f0f0f2, #dedee3); }
  .signer { margin-top: 2px; font-size: 6px; }
  .watermark {
    position: absolute; left: 150px; right: 0; bottom: 64px;
    display: flex; justify-content: center; align-items: center; gap: 10px;
    font-weight: 600; font-size: 28px; color: var(--faint); white-space: nowrap;
  }
  .watermark .square { width: 24px; height: 24px; background: var(--faint); }
  .letterhead .address { bottom: 22px; left: 60px; font-size: 8px; font-weight: 600; }

  /* Envelope back */
  .envelope-back {
    position: absolute; left: 77px; top: 887px; width: 480px; height: 244px;
    background: var(--paper); box-shadow: 0 4px 10px rgba(0,0,0,.2); overflow: hidden;
  }
  .envelope-back svg { position: absolute; inset: 0; }
  .envelope-back .brand { position: absolute; left: 0; right: 0; top: 46px; justify-content: center; font-size: 18px; }
  .envelope-back .brand .square { width: 14px; height: 14px; }

  /* Envelope front */
  .envelope-front {
    position: absolute; left: 634px; top: 887px; width: 480px; height: 244px;
    background: linear-gradient(160deg, #fff 40%, var(--shade)); box-shadow: 0 4px 10px rgba(0,0,0,.2);
    padding: 18px 26px;
  }
  .envelope-front .brand { font-size: 10px; }
  .envelope-front .brand .square { width: 9px; height: 9px; }
  .envelope-front .contact { font-size: 5.5px; }
  .envelope-front .contact .firm { font-size: 6.5px; }
  .side-bar { position: absolute; top: 16px; width: 5px; height: 30px; background: var(--navy); }
  .side-bar.left { left: 0; }
  .side-bar.right { right: 0; }
  .bottom-band { position: absolute; left: 0; right: 0; bottom: 0; height: 20px; background: var(--navy); }
  .envelope-front .address { bottom: 24px; font-size: 5.5px; color: var(--grey); }
</style>
</head>
<body>

<section class="letterhead">
  <header class="header">
    <div class="brand"><span class="square"></span>Tallow &amp; Mersey</div>
    <div class="contact">
      <div class="firm">Tallow &amp; Mersey, LLP</div>
      <div>(555) 408-1936<svg viewBox="0 0 10 10"><path d="M2 1l2 2-1 1.5c.8 1.5 1.5 2.2 3 3L7.5 6.5l2 2L8 10C4 9.5.5 6 0 2z"/></svg></div>
      <div>(555) 408-2275<svg viewBox="0 0 10 10"><rect x="1" y="3" width="8" height="5"/><rect x="3" y="0" width="4" height="3"/></svg></div>
      <div>www.tallowandmersey.example<svg viewBox="0 0 10 10"><circle cx="5" cy="5" r="5"/></svg></div>
    </div>
  </header>

  <div class="body">
    <p>Lorem ipsum dolor sit amet, consectetur adipiscing elit. Donec eget nisi eget tortor iaculis tristique. Aliquam tincidunt posuere tortor hendrerit elementum. Nunc laoreet lorem a sem auctor fringilla. Pellentesque dignissim accumsan lobortis. Sed pharetra erat vitae dui imperdiet quis commodo orci dapibus. Cum sociis natoque penatibus et magnis dis parturient montes, nascetur ridiculus mus. Fusce at nunc libero. Nam metus lorem, rhoncus ac mattis ornare, blandit vel risus.</p>
    <p>Vestibulum ante ipsum primis in faucibus orci luctus et ultrices posuere cubilia Curae; Ut sit amet augue eget purus facilisis suscipit. Sed vitae risus nibh. Vivamus at sollicitudin ipsum. Vestibulum consectetur dictum egestas. Nam eu tortor non mauris condimentum rutrum eu at urna. Vivamus quis odio et velit aliquet adipiscing quis quis diam. Quisque facilisis molestie neque, in consequat tortor viverra eu.</p>
    <p>Etiam tincidunt aliquam porta. Phasellus ut nisi nibh. Pellentesque non nulla nisi. Sed interdum porta leo ut interdum. Integer molestie, libero quis pellentesque gravida, sapien sem varius est, vel sagittis libero sapien id nulla. Vivamus aliquam nulla vitae mi sodales sit amet semper nulla pulvinar. Nulla congue sagittis auctor. Pellentesque sollicitudin mollis libero.</p>
    <div class="closing">Yours faithfully,</div>
    <div class="signature" role="img" aria-label="Handwritten signature"></div>
    <div class="signer">Jordan Avery Doe</div>
  </div>

  <div class="watermark"><span class="square"></span>Tallow &amp; Mersey</div>
  <div class="address">7183 Corvid Lane, Suite 1000, Brenford, TX 75591</div>
</section>

<section class="envelope-back">
  <svg viewBox="0 0 480 244" width="480" height="244" aria-hidden="true">
    <path d="M0 244 L215 112 Q240 98 265 112 L480 244 Z" fill="var(--pocket)"/>
    <path d="M0 0 L0 20 L200 115 Q240 135 280 115 L480 20 L480 0 Z" fill="var(--flap)"/>
    <rect x="0" y="0" width="480" height="12" fill="var(--navy)"/>
  </svg>
  <div class="brand"><span class="square"></span>Tallow &amp; Mersey</div>
</section>

<section class="envelope-front">
  <span class="side-bar left"></span><span class="side-bar right"></span>
  <header class="header">
    <div class="brand"><span class="square"></span>Tallow &amp; Mersey</div>
    <div class="contact">
      <div class="firm">Tallow &amp; Mersey, LLP</div>
      <div>(555) 408-1936</div>
      <div>(555) 408-2275</div>
      <div>www.tallowandmersey.example</div>
    </div>
  </header>
  <div class="address">7183 Corvid Lane, Suite 1000, Brenford, TX 75591</div>
  <div class="bottom-band"></div>
</section>

</body>
</html>
```